依頼詳細
「仙台箪笥」は本来すべてが「手しごと」で作られたものを言います。しかし、近年は工場の機械で大量生産されたものを「仙台箪笥」として販売する企業が増えてきており、「本物」を作る職人達は価格競争で負けてしまいます。そんな中でも、柴崎庵では全ての工程を手しごとで行い、愚直に仙台箪笥を作り続けてきました。今のまま「安かろう、良かろう」の精神で仙台箪笥を販売する企業や、それを購入する消費者が増え続けてしまっては、江戸時代から培われてきた仙台の伝統が途絶えてしまいます。本チラシのデザインでは、そんな時代に警笛を鳴らすようなメッセージを込めて頂きたいと考えております。柴崎庵の代表・柴崎守氏からのメッセージや仙台箪笥の歴史を説明する資料を添付します。そちらを参考に、本物の箪笥の価値を伝えるデザインをして下さった方を採用とさせて頂きます。柴崎氏からの要望は2つあり、「『ずいぶんお堅い感じね』と言われるようなもの』」「伝統工芸をずっと続けてやっているんだなというイメージ」を意識してほしいとのことです。その他、何か質問があればどうぞお気軽にお問い合わせくださいませ。Mail→tokoharuwen@mailbox-demo.jp
記載項目
工房名/仙台箪笥 柴崎庵
住所/添付資料
電話番号/添付資料
ホームページURL・QRコード/現在HPリニューアル中のため、リニューアル完了後にこちらで入れ込みます。入れるスペースを分かるようにしておいてください。
キャッチコピー/デザインに合わせ、「依頼詳細」にある説明を参考に、心に刺さるコピーを入れてください。
写真/添付資料にある、柴崎守氏の写真と仙台箪笥の写真を中心に上手く組み合わせてデザインしてください。

〜コピー参考例〜
(コピーが浮かばなかった場合は、こちらのコピーの中から選んで入れてください。)

・一〇〇年先に繋ぎたい、一〇〇年前の財産
・本物しか作らない、「手しごと」の心
サイズ
A4
ページ数
片面
希望イメージ
シンプル 複雑
単色 カラフル
暗い 明るい
日常 高級
遊び心 厳粛
未来的 伝統的
女性的 男性的
希望する色
仙台箪笥の色にあった色を基調としてください。
納品ファイル
• イラストレーター形式 (.ai)
補足説明
現在リニューアル中ですが、こちらが現在の「柴崎庵」のホームページです。
http://homepage5.example-host.jp/shibasakian/
→ページ左上にあるロゴを使用できれば、デザインの中に入れ込んでほしいです
参考映像
https://www.videoshare-demo.jp/watch?v=Qw3rTz8LmNp
https://www.videoshare-demo.jp/watch?v=Vb6yHs2KoRd

柴崎氏ご本人に選んで頂きました。

この度は多数のご応募、誠にありがとうございました。どの作品も素晴らしいもので、一つに選ぶのが非常に難しかったです。またの機会にも、どうぞご応募頂ければ幸いです。宜しくお願い致します。

```html
<!DOCTYPE html>
<html lang="ja">
<head>
<meta charset="utf-8">
<title>仙台箪笥 柴崎庵</title>
<link rel="stylesheet" href="https://fonts.googleapis.com/css2?family=Shippori+Mincho+B1:wght@500;700;800&family=Noto+Serif+JP:wght@400;600&display=swap">
<style>
  :root{
    --paper:#e9e7e3;
    --paper-mid:#b9b5ae;
    --shadow:#2b2725;
    --night:#121010;
    --ink:#1b1918;
    --ink-soft:#3a3533;
    --light:#f1eee9;
    --light-soft:#c9c4bd;
    --lacquer:#5a1a1c;
    --iron:#1a1413;
  }
  *{margin:0;padding:0;box-sizing:border-box}
  html,body{width:849px;height:1200px;overflow:hidden;background:var(--paper)}
  .flyer{position:relative;width:849px;height:1200px;overflow:hidden;background:var(--paper);font-family:"Noto Serif JP",serif;color:var(--ink)}
  .craftsman-photo{position:absolute;left:0;top:380px;width:849px;height:820px;
    background:linear-gradient(180deg,var(--paper) 0%,var(--paper-mid) 18%,var(--shadow) 42%,var(--night) 100%)}
  .tansu-photo{position:absolute;left:14px;top:0;width:360px;height:362px;
    background:radial-gradient(ellipse at 45% 40%,var(--lacquer) 0%,#3a1214 55%,var(--iron) 100%)}
  .vertical{writing-mode:vertical-rl;text-orientation:upright}
  .brand{position:absolute;left:654px;top:30px;font-family:"Shippori Mincho B1",serif;font-weight:700;font-size:24px;letter-spacing:2px}
  .brand-mark{position:absolute;left:651px;top:142px;width:30px;height:30px;border-radius:50%;background:var(--ink)}
  .headline{position:absolute;font-family:"Shippori Mincho B1",serif;font-weight:800;font-size:54px;line-height:1;letter-spacing:-3px;color:var(--ink)}
  .headline.first{left:572px;top:26px}
  .headline.second{left:482px;top:78px}
  .message-title{position:absolute;left:452px;top:290px;font-family:"Shippori Mincho B1",serif;font-weight:700;font-size:21px;letter-spacing:3px;color:var(--ink-soft)}
  .message-body{position:absolute;left:282px;top:378px;width:160px;height:150px;font-size:10.5px;line-height:17px;color:var(--ink-soft)}
  .workshop{position:absolute;left:14px;top:636px;width:256px}
  .workshop-photo{width:156px;height:72px;background:linear-gradient(180deg,#8a8782,#4a4642)}
  .workshop-name{margin-top:18px;font-family:"Shippori Mincho B1",serif;font-weight:700;font-size:22px;color:var(--light);letter-spacing:1px}
  .workshop-info{margin-top:8px;font-size:9.5px;line-height:15px;color:var(--light-soft)}
  .url-space{margin-top:10px;width:64px;height:64px;border:1px solid var(--light-soft)}
  .profile{position:absolute;left:440px;top:704px;width:380px;color:var(--light)}
  .profile-title{font-size:13px;letter-spacing:1px}
  .profile-title .name{font-family:"Shippori Mincho B1",serif;font-weight:700;font-size:17px;margin-left:6px}
  .profile-title .roman{font-size:10px;margin-left:6px;color:var(--light-soft)}
  .profile-text{margin-top:10px;font-size:10.5px;line-height:18px;color:var(--light-soft)}
</style>
</head>
<body>
<div class="flyer">
  <div class="craftsman-photo" role="img" aria-label="工房で作業する仙台箪笥職人・柴崎守氏の写真"></div>
  <div class="tansu-photo" role="img" aria-label="黒漆塗りに鉄金具の仙台箪笥の写真"></div>

  <div class="brand vertical">仙台箪笥</div>
  <div class="brand-mark"></div>

  <h1>
    <span class="headline first vertical">百年続く、</span>
    <span class="headline second vertical">「手しごと」の心</span>
  </h1>

  <h2 class="message-title vertical">柴崎 守の想い</h2>
  <p class="message-body vertical">仙台箪笥は本来、すべての工程を職人の手で仕上げるものです。木地づくり、漆塗り、金具の打ち出し。ひとつひとつに時間をかけ、百年使える道具を作ってきました。安さだけを求める時代に、本物の価値をもう一度見つめてほしい。江戸から受け継いだこの技を、次の百年へ手渡すために、今日も鉋を手に取ります。</p>

  <div class="workshop">
    <div class="workshop-photo" role="img" aria-label="柴崎庵の工房外観の写真"></div>
    <div class="workshop-name">仙台箪笥 柴崎庵</div>
    <p class="workshop-info">〒980-0000<br>宮城県仙台市青葉区中町0-0-0<br>TEL 022-000-0000<br>FAX 022-000-0001</p>
    <div class="url-space" aria-label="ホームページQRコード掲載スペース"></div>
  </div>

  <div class="profile">
    <p class="profile-title">仙台箪笥職人<span class="name">柴崎 守</span><span class="roman">Mamoru Shibasaki</span></p>
    <p class="profile-text">1957年仙台市生まれ。仙台箪笥の工房を営む父に師事し、修業を重ねる。伝統の技法を守りながら、全工程を手しごとで仕上げる箪笥作りを続けている。2014年には海外の工芸展に出品し、国内外から注目を集めている。</p>
  </div>
</div>
</body>
</html>
```